Website Design for Chef Wirra Chinese Restaurant

Chef Wirra is a new Chinese Restaurant. It offers exceptional dining experience with authentic and dynamic dishes created with quality ingredients.

A vivid website theme is required to promote this new restaurant online. Logo, menu, wine list and a few other files are attached for help with designing.

A very rough demo website has been setup and can be accessed via http://www.chefwirra.com.au. It is for telling designers what content is shown up on each page (except for homepage). By reading the about us page, designers can get some more info of Chef Wirra. However, the layout, theme color, font, etc are not set in stone. Visitors should be able to feel Chef Wirra restaurant's authentic Chinese cuisine and high hygiene standard. Home page of the website could be The "Our website is coming soon" description is shown on demo site but do not required to be presented on new design.

Some main pages design should be included: Home (landing page), About us, Menu (Dishes), Winelist, Gallery, Contact us. No HTML and coding required. The output should be well layered psd or png files with acceptable resolution for web use.

A few other website can be referred to are:

http://kelpmerachinese.com.au/
http://www.stone-lamp.com/
http://brimvale.com.au/
http://harvelrestaurant.com.au/
http://www.tilmorerestaurant.com.au/
http://www.thequill.com.au/

Industry/Entity Type

Restaurant

Requirements
Nice to have
• I expect designs of at least these webpages: homepage, menu page and contact us page. If you can provide "about us" page as well, it will probably help you win the competition. well layered psd or png file is my preference.
Should not have
• You don't have to make html/cs/js or any coding. All I need is just art design

```html
<!DOCTYPE html>
<html lang="en">
<head>
<meta charset="utf-8">
<title>Chef Wirra Chinese Restaurant</title>
<link href="https://fonts.googleapis.com/css2?family=Cinzel:wght@400;700&family=Open+Sans:wght@400;600;700&display=swap" rel="stylesheet">
<style>
:root{
  --red:#ee1c1c;
  --red-dark:#c40f0f;
  --cream:#fdf8c6;
  --grey-frame:#b3b3b3;
  --text:#555;
  --heading:#333;
  --footer:#2c2c2c;
  --footer-deep:#121212;
  --white:#fff;
}
*{margin:0;padding:0;box-sizing:border-box}
html,body{width:697px;height:1200px;overflow:hidden;background:var(--white)}
body{position:relative;font-family:'Open Sans',sans-serif;color:var(--text)}
.abs{position:absolute}
.top-strip{left:0;top:0;width:697px;height:8px;background:var(--red)}
.header{left:0;top:8px;width:697px;height:145px;background:var(--cream)}
.brand{left:66px;top:40px;display:flex;align-items:center;gap:7px}
.brand-mark{width:18px;height:18px;background:var(--red)}
.brand-name{font-family:'Cinzel',serif;font-weight:700;font-size:12px;color:var(--red);line-height:1.15;width:120px}
.social{left:491px;top:33px;display:flex;gap:6px}
.social span{width:20px;height:20px;border-radius:50%;background:var(--red);display:block}
.contact-phone{left:334px;top:57px;display:flex;align-items:flex-start;gap:5px}
.contact-phone .num{font-size:15px;color:#555;line-height:1}
.contact-phone .mail{font-size:7px;color:#666;margin-top:3px}
.search{left:487px;top:61px;width:132px;height:24px;border:2px solid #f0e3a3;border-radius:3px;background:#f8efb4}
.search .field{position:absolute;left:3px;top:3px;width:106px;height:15px;background:var(--white);border-radius:7px;font-size:6.5px;color:#aaa;padding:3px 6px}
.search svg{position:absolute;right:4px;top:5px}
.paper{left:90px;top:103px;width:518px;height:62px;background:var(--white)}
.nav-band{left:85px;top:117px;width:527px;height:34px;background:var(--red);display:flex;align-items:center;justify-content:space-around;padding:0 22px}
.nav-band a{color:var(--white);font-size:7.2px;font-weight:700;text-decoration:none;letter-spacing:.2px}
.hero{left:0;top:153px;width:697px;height:298px;background:radial-gradient(ellipse at 50% 55%,#7a4a35 0%,#5b4a2c 30%,#d9d4cc 62%,#6c6660 100%)}
.hero-caption{left:207px;top:257px;width:280px;height:61px;background:rgba(40,40,30,.55);display:flex;align-items:center;justify-content:center;text-align:center;font-family:'Cinzel',serif;font-size:14.5px;color:var(--white);line-height:1}
.hero-arrow{top:277px}
.feature{top:438px;width:161px;height:160px;border:5px solid var(--grey-frame);background:var(--white);box-shadow:0 12px 8px -8px rgba(0,0,0,.25);text-align:center}
.feature .pic{height:94px;border-bottom:1px solid #ccc;margin:0 0 6px}
.feature h3{font-weight:400;font-size:10px;color:var(--red);margin-bottom:3px}
.feature p{font-size:7px;line-height:1.8;color:#777;padding:0 18px}
.welcome{left:0;top:624px;width:697px;text-align:center;font-family:'Cinzel',serif;font-size:13.5px;color:var(--heading)}
.intro{left:95px;top:658px;width:507px;text-align:center;font-size:6.9px;line-height:2.15;color:#666}
.section-title{left:79px;top:729px;font-family:'Cinzel',serif;font-size:13px;color:var(--heading)}
.post{top:770px;width:133px;height:230px;border:1px solid #ccc;text-align:center;background:var(--white)}
.post .pic{height:113px}
.post h4{font-weight:400;font-size:9px;color:var(--red);margin:7px 0 6px}
.post p{font-size:7.1px;line-height:2.05;color:#555;padding:0 6px}
.post .btn{display:inline-block;margin-top:9px;background:var(--red);color:var(--white);font-size:6.6px;padding:4px 7px}
.footer{left:0;top:1025px;width:697px;height:140px;background:var(--footer);color:var(--white)}
.col{position:absolute;top:14px;font-size:6.6px;line-height:1.75}
.col h5{font-weight:600;font-size:10px;margin-bottom:4px}
.col b{display:block;font-size:8px;margin-top:4px}
.event{display:flex;gap:7px;align-items:flex-start;margin-top:7px}
.date{width:29px;text-align:center}
.date .m{background:var(--red);font-weight:700;font-size:6.5px;padding:1px 0}
.date .d{background:#555;font-weight:700;font-size:6.5px;padding:3px 0}
.rule{height:1px;background:#555;margin:9px 0 0;width:112px}
.input{width:121px;height:14px;background:#444;font-size:6.5px;color:#888;padding:2px 4px;margin-top:6px}
.submit{display:inline-block;margin-top:8px;background:var(--red);font-size:7px;padding:2px 6px}
.bottom{left:0;top:1165px;width:697px;height:35px;background:var(--footer-deep);color:var(--white);font-size:7px;text-align:center;line-height:35px}
</style>
</head>
<body>
<div class="abs top-strip"></div>
<header class="abs header"></header>
<div class="abs brand"><span class="brand-mark"></span><span class="brand-name">Chef Wirra Chinese Restaurant</span></div>
<div class="abs social"><span></span><span></span><span></span><span></span><span></span></div>
<div class="abs contact-phone">
  <svg width="16" height="16" viewBox="0 0 16 16"><circle cx="8" cy="8" r="7" fill="none" stroke="#ee1c1c" stroke-width="1.4"/><path d="M5.5 4.5l1.5 1.5-1 1.2c.5 1.2 1.4 2.1 2.6 2.6l1.2-1 1.5 1.5-1 1.2c-2.6-.3-4.8-2.5-5.1-5.1z" fill="#ee1c1c"/></svg>
  <div><div class="num">08 9471 2265</div><div class="mail">info@ChefWirraRestaurant.com.au</div></div>
</div>
<div class="abs search"><div class="field">SEARCH</div>
  <svg width="11" height="11" viewBox="0 0 11 11"><circle cx="4.5" cy="4.5" r="3.3" fill="none" stroke="#777" stroke-width="1.4"/><path d="M7 7l3 3" stroke="#777" stroke-width="1.6"/></svg>
</div>
<div class="abs paper"></div>
<svg class="abs" style="left:52px;top:112px" width="593" height="44" viewBox="0 0 593 44">
  <polygon points="0,5 38,5 38,39 0,39 14,22" fill="#ee1c1c"/>
  <polygon points="593,5 555,5 555,39 593,39 579,22" fill="#ee1c1c"/>
  <polygon points="33,5 38,5 38,0" fill="#8a0a0a"/>
  <polygon points="560,5 555,5 555,0" fill="#8a0a0a"/>
</svg>
<nav class="abs nav-band">
  <a href="#">HOME</a><a href="#">ABOUT US</a><a href="#">MENU</a><a href="#">WINE LIST</a><a href="#">GALLERY</a><a href="#">CONTACT US</a><a href="#">KELPMERA COURT</a>
</nav>
<div class="abs hero" role="img" aria-label="Bowl of noodles with sliced beef, greens and red chilli"></div>
<div class="abs hero-caption">MINCED PORK &amp; PEANUT<br>DUMPLINGS</div>
<svg class="abs hero-arrow" style="left:32px" width="18" height="22" viewBox="0 0 18 22"><path d="M14 2L4 11l10 9" fill="none" stroke="#fff" stroke-width="4"/></svg>
<svg class="abs hero-arrow" style="left:652px" width="18" height="22" viewBox="0 0 18 22"><path d="M4 2l10 9-10 9" fill="none" stroke="#fff" stroke-width="4"/></svg>

<div class="abs feature" style="left:100px"><div class="pic" role="img" aria-label="Spicy chicken feet in a bamboo steamer" style="background:radial-gradient(circle,#d8452a 0%,#c98a4a 45%,#fff 72%)"></div><h3>SPICY CHICKEN FEET</h3><p>nulidas vacsques asey yoleacene anris ma hasease.</p></div>
<div class="abs feature" style="left:268px"><div class="pic" role="img" aria-label="Deep fried dough sticks on a plate" style="background:radial-gradient(ellipse,#d98a3a 0%,#e7c58f 40%,#fff 70%)"></div><h3>DEEP FRIED DOUGH STICKS</h3><p>nulidas vacsques asey yoleacene anris ma hasease.</p></div>
<div class="abs feature" style="left:436px"><div class="pic" role="img" aria-label="Wonton noodle soup in a white bowl" style="background:radial-gradient(ellipse,#c7a57a 0%,#e5e2da 45%,#fff 70%)"></div><h3>WONTON NOODLE SOUP</h3><p>nulidas vacsques asey yoleacene anris ma hasease.</p></div>

<h1 class="abs welcome" style="font-weight:400">WELCOME TO&nbsp; CHEF WIRRA CHINESE RESTAURANT</h1>
<p class="abs intro">Beciegast kiausnveriti vitaesaert asety kertya aset aplica bosafae keuestyasne moseade keryiuasa doloertymuas faserani ptaiades kertyaser daesraeds. Casrolern atur aut oditaut. onsequuntur magni dolqui ratione voluptatemsequi nesrentro quiserstqui dosum, quia dolor asasaert nsectetur adipivelisuia non numquam eius modi teincidunt, ut labore et dolore magnam.</p>
<h2 class="abs section-title" style="font-weight:400">OUR LATEST POST</h2>

<div class="abs post" style="left:76px"><div class="pic" role="img" aria-label="Steamed pork ribs in a bamboo steamer" style="background:radial-gradient(circle,#8a4e2c 0%,#d9a162 45%,#fff 72%)"></div><h4>STEAMED PORK RIBS</h4><p>Vaserbo nerafaes akerts vitaeerty asnemo lasec vasptaia goertayse. maloreo qui ratione voluptate</p><span class="btn">READ MORE</span></div>
<div class="abs post" style="left:214px"><div class="pic" role="img" aria-label="Fried white radish cakes" style="background:radial-gradient(ellipse,#e2a25a 0%,#f1d2a6 45%,#fff 75%)"></div><h4>FRIED WHITE RADISH PATEY</h4><p>Vaserbo nerafaes akerts vitaeerty asnemo lasec vasptaia goertayse. maloreo qui ratione voluptate</p><span class="btn">READ MORE</span></div>
<div class="abs post" style="left:351px"><div class="pic" role="img" aria-label="Coral trout with ginger on a plate" style="background:linear-gradient(160deg,#f2ece6 0%,#e7a69a 50%,#c9463a 100%)"></div><h4>CORAL TROUTWITH GNGER</h4><p>Vaserbo nerafaes akerts vitaeerty asnemo lasec vasptaia goertayse. maloreo qui ratione voluptate</p><span class="btn">READ MORE</span></div>
<div class="abs post" style="left:488px"><div class="pic" role="img" aria-label="Abalone noodles in a golden bowl" style="background:radial-gradient(circle,#e0902a 0%,#b9681e 45%,#3a2414 85%)"></div><h4>ABALONE NOODLES</h4><p>Vaserbo nerafaes akerts vitaeerty asnemo lasec vasptaia goertayse. maloreo qui ratione voluptate</p><span class="btn">READ MORE</span></div>

<footer class="abs footer">
  <div class="col" style="left:75px"><h5>TRADING HOURS</h5>We are open 7 days<b>Lunch</b>Monday to Friday 11:30am - 2:30pm<br>Saturday to Sunday 11:00am - 3:00pm<b>Dinner</b>Monday to Sunday 6:00pm</div>
  <div class="col" style="left:228px"><h5>CONTACTS</h5>4/217 Marlowe Road<br>Eastgrove,<br>SA, 5081<b>Phone</b>08 8275 3319<br>08 9471 2265</div>
  <div class="col" style="left:349px"><h5>UPCOMING EVENTS</h5>
    <div class="event"><div class="date"><div class="m">NOV</div><div class="d">23</div></div><div>Friday's at the Quill<br>Time: 5:00 pm</div></div>
    <div class="rule"></div>
    <div class="event"><div class="date"><div class="m">NOV</div><div class="d">23</div></div><div>Departure Saturday<br>Time: 5:00 pm</div></div>
  </div>
  <div class="col" style="left:485px;top:12px"><h5>NEWSLETTER</h5>Sign up for our newsletter and get the latest news.<div class="input">Name</div><div class="input">Email</div><span class="submit">Submit</span></div>
</footer>
<div class="abs bottom">© 2014 - Chef Wirra Chinese Restaurant</div>
</body>
</html>
```